DJ business brochure

I need a business brochure for my DJ business. Something that represents my business being owned and operated by first responders yet elegant enough to attract customers for weddings.

I do not have a preference on a type of brochure. Tri-fold or standard. The front page should have our logo and the name of our company. Under the name of our company it should say "Owned and operated by First Responders"

Bullet points for the brochure
LED up lighting.
Video projection
Dancing in the clouds
Top rated and experienced DJ's
Fun, crowd interactive DJ's
Text song request line.
Professional reception planning.

It should say somewhere on the brochure "When you choose Ember Deck you become part of the first responder family."

Contact information Rob@emberdeckdj.net Phone or text (738) 261-4907

Please use some fun pictures of weddings or people dancing. Does not specifically need to be from our sites.

Target Market(s)

Brides/Groom

Industry/Entity Type

Wedding/Party DJ

Requirements
Must have
• I want the wow factor. Something that when people look at the brochure they are drawn to read it. Email Rob@EmberDeckDJ.net Phone (738) 261-4907
Nice to have
• Nice to have a flaming vinyl record or a flaming musical note somewhere in the brochure.

```html
<!DOCTYPE html>
<html lang="en">
<head>
<meta charset="utf-8">
<title>Ember Deck – DJ Brochure</title>
<link href="https://fonts.googleapis.com/css2?family=Exo+2:ital,wght@0,800;1,700;1,800&family=Poppins:ital,wght@0,400;0,600;1,400;1,600;1,700&display=swap" rel="stylesheet">
<style>
  :root{
    --red:#e01a1f;
    --red-deep:#b80f14;
    --black:#0d0d0e;
    --panel:#141416;
    --row:#2b2b2e;
    --grey:#8a8a8d;
    --white:#ffffff;
    --page:#eef0f3;
  }
  *{margin:0;padding:0;box-sizing:border-box}
  html,body{width:1200px;height:2333px;overflow:hidden}
  body{background:var(--page);font-family:"Poppins",sans-serif;color:var(--white);position:relative}
  .spread{position:absolute;left:50px;width:1100px;height:778px;display:flex;box-shadow:0 10px 24px rgba(0,0,0,.35);overflow:hidden;background:var(--black)}
  .spread--outside{top:328px}
  .spread--inside{top:1226px}
  .panel{position:relative;width:366.67px;height:100%;overflow:hidden}
  .panel--dark{background:linear-gradient(180deg,#1b1b1d 0%,#0b0b0c 100%)}
  .panel--red{background:var(--red)}
  .photo{position:absolute;display:block}
  .heading{font-family:"Exo 2",sans-serif;font-style:italic;font-weight:800;text-transform:uppercase;line-height:1;letter-spacing:.5px}
  .heading .red{color:var(--red)}
  .body-copy{font-style:italic;font-size:10.6px;line-height:1.2;text-align:justify;color:#e6e6e6}
  .brand{display:flex;align-items:center;gap:8px;font-family:"Exo 2",sans-serif;font-weight:800;text-transform:uppercase;color:var(--white);font-size:22px;letter-spacing:1px}
  .brand-dot{width:14px;height:14px;border-radius:50%;background:var(--red)}

  /* outside – left panel */
  .choose{position:absolute;left:42px;top:58px;width:290px}
  .choose .kicker{font-size:23px}
  .choose .name{font-size:46px;color:var(--red);margin-top:2px}
  .choose .family{font-size:16px;margin-top:22px;line-height:1.05}
  .choose .body-copy{margin-top:26px}

  /* outside – contact panel */
  .contact{position:absolute;inset:0;display:flex;flex-direction:column;align-items:center}
  .contact .brand{margin-top:340px}
  .contact-item{display:flex;flex-direction:column;align-items:center;font-style:italic}
  .contact-item svg{width:28px;height:28px;margin-bottom:8px}
  .phone{margin-top:74px;font-weight:700;font-size:27px}
  .email{margin-top:30px;font-size:19px}
  .web{margin-top:30px;font-size:19px}

  /* outside – cover */
  .cover .brand{position:absolute;top:100px;left:0;right:0;justify-content:center;font-size:26px}
  .cover-title{position:absolute;left:48px;top:585px;width:280px}
  .cover-title .l1{font-size:39px}
  .cover-title .l2{font-size:30px;color:var(--red)}
  .cover-title .bar{display:inline-block;margin-top:8px;background:var(--red);font-size:20px;letter-spacing:7px;padding:3px 18px 3px 18px;width:264px;text-align:center}
  .cover-url{position:absolute;left:0;right:0;top:732px;text-align:center;font-style:italic;font-size:15px;letter-spacing:1px}
  .cover-url b{font-weight:700}

  /* inside */
  .intro{position:absolute;left:40px;top:55px;width:282px}
  .intro .kicker{font-size:22px}
  .intro .big{font-size:35px;color:var(--red);line-height:.98}
  .intro .body-copy{margin-top:28px}
  .intro .body-copy + .body-copy{margin-top:20px}

  .using{position:absolute;left:38px;top:55px;width:288px}
  .using .kicker{font-size:22px}
  .using .big{font-size:22px;color:var(--red)}
  .checklist{list-style:none;margin-top:22px}
  .checklist li{display:flex;align-items:center;gap:10px;font-style:italic;font-weight:700;font-size:10px;height:25.5px}
  .checklist svg{width:15px;height:15px;flex:none}
  .using .body-copy{margin-top:24px}
  .using .body-copy + .body-copy{margin-top:20px}

  .packages{position:absolute;left:38px;top:55px;width:290px}
  .packages .kicker{font-size:22px}
  .pkg-title{font-family:"Exo 2",sans-serif;font-style:italic;font-weight:800;color:var(--red);font-size:16px;margin:26px 0 10px}
  .pkg-list{list-style:none}
  .pkg-list li{display:flex;justify-content:space-between;align-items:center;height:25px;padding:0 16px 0 12px;font-style:italic;font-size:10.5px;width:275px}
  .pkg-list li:nth-child(odd){background:linear-gradient(90deg,#3a3a3d,#2a2a2c)}
  .pkg-list li b{font-weight:700;font-size:10px}

  .footer-band{position:absolute;left:397px;right:0;bottom:12px;height:44px;background:var(--red);clip-path:polygon(40px 0,100% 0,100% 100%,0 100%)}
  .footer-grey{position:absolute;right:0;bottom:12px;width:80px;height:44px;background:#6d6d70;clip-path:polygon(45px 0,100% 0,100% 100%,0 100%)}
  .footer-line{position:absolute;left:0;right:0;bottom:6px;height:6px;background:var(--red)}
  .footer-url{position:absolute;bottom:22px;font-style:italic;font-size:15px;letter-spacing:1px}
  .footer-url b{font-weight:700}
  .footer-url--mid{left:460px}
  .footer-url--right{left:825px}
</style>
</head>
<body>

<!-- Outside spread -->
<section class="spread spread--outside">
  <article class="panel panel--dark">
    <div class="choose">
      <h2 class="heading kicker">When you choose</h2>
      <h1 class="heading name">Ember Deck</h1>
      <p class="heading family">You become part of the<br>first responder family</p>
      <p class="body-copy">Lorem ipsum dolor sit amet, consectetur adipiscing elit. Vestibulum magna leo, malesuada sed tincidunt id, facilisis a ipsum. Class aptent taciti sociosqu ad litora torquent per conubia nostra, per inceptos himenaeos. Nunc condimentum cursus mauris, a sollicitudin magna fringilla ac. Aenean pharetra eros in elit vehicula, vel luctus enim congue. Phasellus congue neque id metus sollicitudin fermentum. Phasellus quis lacinia urna. Aenean nisl lorem, commodo eu odio vitae, mollis cursus nisl.</p>
    </div>
    <svg class="photo" role="img" aria-label="Photo of a smiling DJ in headphones at the decks under blue and purple light" style="left:0;top:368px;width:366.67px;height:410px" viewBox="0 0 100 100" preserveAspectRatio="none">
      <defs><radialGradient id="djBlue" cx="50%" cy="45%" r="65%"><stop offset="0" stop-color="#3a4f86"/><stop offset=".5" stop-color="#241c48"/><stop offset="1" stop-color="#0b0b0c"/></radialGradient></defs>
      <rect width="100" height="100" fill="url(#djBlue)"/>
    </svg>
  </article>

  <article class="panel panel--red">
    <svg class="photo" role="img" aria-label="Red-toned photo of a DJ's hand on a mixing console" style="inset:0;width:100%;height:100%" viewBox="0 0 100 100" preserveAspectRatio="none">
      <defs><linearGradient id="redTone" x1="0" y1="0" x2="0" y2="1"><stop offset="0" stop-color="#c8161b"/><stop offset=".45" stop-color="#d8191e"/><stop offset="1" stop-color="#e01a1f"/></linearGradient></defs>
      <rect width="100" height="100" fill="url(#redTone)"/>
    </svg>
    <div class="contact">
      <div class="brand"><span class="brand-dot"></span>Ember Deck</div>
      <div class="contact-item phone">
        <svg viewBox="0 0 24 24"><path fill="#fff" d="M6.6 10.8a15.1 15.1 0 0 0 6.6 6.6l2.2-2.2a1 1 0 0 1 1-.25 11.4 11.4 0 0 0 3.6.57 1 1 0 0 1 1 1V20a1 1 0 0 1-1 1A17 17 0 0 1 3 4a1 1 0 0 1 1-1h3.5a1 1 0 0 1 1 1c0 1.25.2 2.45.57 3.6a1 1 0 0 1-.25 1z"/></svg>
        (738) 261-4907
      </div>
      <div class="contact-item email">
        <svg viewBox="0 0 24 24"><rect x="2" y="5" width="20" height="14" fill="#fff"/><path d="M2 5l10 8 10-8" fill="none" stroke="#e01a1f" stroke-width="1.6"/></svg>
        Rob@EmberDeckDJ.net
      </div>
      <div class="contact-item web">
        <svg viewBox="0 0 24 24" fill="none" stroke="#fff" stroke-width="1.8"><circle cx="12" cy="12" r="9"/><ellipse cx="12" cy="12" rx="4" ry="9"/><path d="M3 12h18M5 7h14M5 17h14"/></svg>
        www.EmberDeckDJ.net
      </div>
    </div>
  </article>

  <article class="panel cover">
    <svg class="photo" role="img" aria-label="Photo of a DJ at the decks framed by a glowing pink neon triangle, with fiery embers and smoke above" style="inset:0;width:100%;height:100%" viewBox="0 0 100 100" preserveAspectRatio="none">
      <defs>
        <linearGradient id="fire" x1="0" y1="0" x2="0" y2="1"><stop offset="0" stop-color="#7a2a10"/><stop offset=".18" stop-color="#3b1a12"/><stop offset=".45" stop-color="#3a3036"/><stop offset=".7" stop-color="#1b1619"/><stop offset="1" stop-color="#0b0b0c"/></linearGradient>
        <radialGradient id="neon" cx="50%" cy="55%" r="35%"><stop offset="0" stop-color="#c4567c" stop-opacity=".55"/><stop offset="1" stop-color="#c4567c" stop-opacity="0"/></radialGradient>
      </defs>
      <rect width="100" height="100" fill="url(#fire)"/>
      <rect width="100" height="100" fill="url(#neon)"/>
    </svg>
    <div class="brand"><span class="brand-dot"></span>Ember Deck</div>
    <div class="cover-title">
      <div class="heading l1">DJ Sounds</div>
      <div class="heading l2">Lights Services</div>
      <div class="heading bar">For Wedding</div>
    </div>
    <p class="cover-url">www.<b>emberdeckdj</b>.net</p>
  </article>
</section>

<!-- Inside spread -->
<section class="spread spread--inside">
  <article class="panel panel--dark">
    <div class="intro">
      <h2 class="heading kicker">Owned &amp; Operated</h2>
      <h1 class="heading big">By First<br>Responders</h1>
      <p class="body-copy">Lorem ipsum dolor sit amet, consectetur adipiscing elit. Vestibulum magna leo, malesuada sed tincidunt id, facilisis a ipsum. Class aptent taciti sociosqu ad litora torquent per conubia nostra, per inceptos himenaeos. Nunc condimentum cursus mauris, a sollicitudin magna fringilla ac. Aenean pharetra eros in elit vehicula, vel luctus enim congue. Phasellus congue neque id metus sollicitudin fermentum. Phasellus quis lacinia urna. Aenean nisl lorem, commodo eu odio vitae, mollis cursus nisl.</p>
      <p class="body-copy">Lorem ipsum dolor sit amet, consectetur adipiscing elit. Vestibulum magna leo, malesuada sed tincidunt id, facilisis a ipsum. Class aptent taciti sociosqu ad litora torquent per conubia nostra, per inceptos himenaeos. Nunc condimentum cursus mauris, a sollicitudin magna fringilla ac. Aenean pharetra eros in elit vehicula, vel luctus enim congue. Phasellus congue neque id metus sollicitudin fermentum. Phasellus quis lacinia urna. Aenean nisl lorem, commodo eu odio vitae, mollis cursus nisl.</p>
    </div>
    <svg class="photo" role="img" aria-label="Photo of a DJ with blue hair and sunglasses at the decks, crowd hands raised in blue smoke" style="left:0;top:493px;width:366.67px;height:285px" viewBox="0 0 100 100" preserveAspectRatio="none">
      <defs><radialGradient id="crowd" cx="50%" cy="55%" r="60%"><stop offset="0" stop-color="#c8962a"/><stop offset=".3" stop-color="#2f5f9a"/><stop offset=".7" stop-color="#162848"/><stop offset="1" stop-color="#0b0b0c"/></radialGradient></defs>
      <rect width="100" height="100" fill="url(#crowd)"/>
    </svg>
  </article>

  <article class="panel panel--dark">
    <div class="using">
      <h2 class="heading kicker">We are</h2>
      <h1 class="heading big">Using</h1>
      <ul class="checklist">
        <li><svg viewBox="0 0 16 16"><circle cx="8" cy="8" r="7" fill="none" stroke="#e01a1f" stroke-width="1.4"/><path d="M4.8 8.2l2.2 2.2 4.2-4.6" fill="none" stroke="#e01a1f" stroke-width="1.5"/></svg>LED up lighting.</li>
        <li><svg viewBox="0 0 16 16"><circle cx="8" cy="8" r="7" fill="none" stroke="#e01a1f" stroke-width="1.4"/><path d="M4.8 8.2l2.2 2.2 4.2-4.6" fill="none" stroke="#e01a1f" stroke-width="1.5"/></svg>Video projection</li>
        <li><svg viewBox="0 0 16 16"><circle cx="8" cy="8" r="7" fill="none" stroke="#e01a1f" stroke-width="1.4"/><path d="M4.8 8.2l2.2 2.2 4.2-4.6" fill="none" stroke="#e01a1f" stroke-width="1.5"/></svg>Dancing in the clouds</li>
        <li><svg viewBox="0 0 16 16"><circle cx="8" cy="8" r="7" fill="none" stroke="#e01a1f" stroke-width="1.4"/><path d="M4.8 8.2l2.2 2.2 4.2-4.6" fill="none" stroke="#e01a1f" stroke-width="1.5"/></svg>Top rated and experienced DJ's</li>
        <li><svg viewBox="0 0 16 16"><circle cx="8" cy="8" r="7" fill="none" stroke="#e01a1f" stroke-width="1.4"/><path d="M4.8 8.2l2.2 2.2 4.2-4.6" fill="none" stroke="#e01a1f" stroke-width="1.5"/></svg>Fun, crowd interactive DJ's</li>
        <li><svg viewBox="0 0 16 16"><circle cx="8" cy="8" r="7" fill="none" stroke="#e01a1f" stroke-width="1.4"/><path d="M4.8 8.2l2.2 2.2 4.2-4.6" fill="none" stroke="#e01a1f" stroke-width="1.5"/></svg>Text song request line.</li>
        <li><svg viewBox="0 0 16 16"><circle cx="8" cy="8" r="7" fill="none" stroke="#e01a1f" stroke-width="1.4"/><path d="M4.8 8.2l2.2 2.2 4.2-4.6" fill="none" stroke="#e01a1f" stroke-width="1.5"/></svg>Professional reception planning.</li>
      </ul>
      <p class="body-copy">Lorem ipsum dolor sit amet, consectetur adipiscing elit. Vestibulum magna leo, malesuada sed tincidunt id, facilisis a ipsum. Class aptent taciti sociosqu ad litora torquent per conubia nostra, per inceptos himenaeos. Nunc condimentum cursus mauris, a sollicitudin magna fringilla ac. Aenean pharetra eros in elit vehicula, vel luctus enim congue. Phasellus congue neque id metus sollicitudin fermentum. Phasellus quis lacinia urna. Aenean nisl lorem, commodo eu odio vitae, mollis cursus nisl. Lorem ipsum dolor sit amet, consectetur adipiscing elit. Vestibulum magna leo, malesuada sed tincidunt id, facilisis a ipsum. Class aptent taciti sociosqu ad litora torquent per conubia nostra, per inceptos himenaeos. Nunc condimentum cursus mauris, a sollicitudin magna fringilla ac. Aenean pharetra eros in elit vehicula, vel luctus enim congue. Phasellus congue neque id metus sollicitudin fermentum. Phasellus quis lacinia urna. Aenean nisl lorem, commodo eu odio vitae, mollis cursus nisl.</p>
      <p class="body-copy">Consectetur adipiscing elit. Vestibulum magna leo, malesuada sed tincidunt id, facilisis a ipsum. Class aptent taciti sociosqu ad litora torquent per conubia nostra, per inceptos himenaeos. Nunc condimentum cursus mauris, a sollicitudin magna fringilla ac. Aenean pharetra eros in elit vehicula, vel luctus enim congue. Phasellus congue neque id metus sollicitudin fermentum. Phasellus quis lacinia urna. Aenean nisl lorem, commodo eu odio vitae, mollis cursus nisl.</p>
    </div>
  </article>

  <article class="panel panel--dark">
    <div class="packages">
      <h2 class="heading kicker">Our <span class="red">Packages</span></h2>
      <h3 class="pkg-title">PACKAGE 1</h3>
      <ul class="pkg-list">
        <li>Lorem ipsum<b>$10</b></li><li>Lorem ipsum<b>$10</b></li><li>Lorem ipsum<b>$10</b></li><li>Lorem ipsum<b>$10</b></li><li>Lorem ipsum<b>$10</b></li>
      </ul>
      <h3 class="pkg-title">PACKAGE 2</h3>
      <ul class="pkg-list">
        <li>Lorem ipsum<b>$10</b></li><li>Lorem ipsum<b>$10</b></li><li>Lorem ipsum<b>$10</b></li><li>Lorem ipsum<b>$10</b></li><li>Lorem ipsum<b>$10</b></li><li>Lorem ipsum<b>$10</b></li><li>Lorem ipsum<b>$10</b></li>
      </ul>
      <h3 class="pkg-title">PACKAGE 3</h3>
      <ul class="pkg-list">
        <li>Lorem ipsum<b>$10</b></li><li>Lorem ipsum<b>$10</b></li><li>Lorem ipsum<b>$10</b></li><li>Lorem ipsum<b>$10</b></li><li>Lorem ipsum<b>$10</b></li>
      </ul>
    </div>
  </article>

  <div class="footer-line"></div>
  <div class="footer-band"></div>
  <div class="footer-grey"></div>
  <p class="footer-url footer-url--mid">www.<b>emberdeckdj</b>.net</p>
  <p class="footer-url footer-url--right">www.<b>emberdeckdj</b>.net</p>
</section>

</body>
</html>
```